Online Banner and skyscrapper ads

Design ads for real estate company in Australia to be used on Plot fnder.com.au details below
sizes
Leaderboard Specifications
• Dimensions: 728×90px
• Format: HTML5 or Animated/Static Gif
• Max file size: 100kb (HTML5), 80kb (GIF, JPG, PNG)
• Back-up image: 40kb (GIF, JPG, PNG). Back-up image only required if you supply an HTML5 banner.
• Looping: Yes
• See Leaderboard for more information.
Email Alert Strip Ad (EASA) Specifications
• Dimensions: 472×114 px
• Format: JPEG, PNG or Static GIF
• File Size: 20kb
• Looping: No
Skyscraper Specifications
• Dimensions: 160x600px
• Looping: Yes
• See Skyscraper for more information.
Mega Skyscraper Specifications
• Dimensions: 300x600px
• Format: HTML5 or Animated/Static GIF
• File size: 100kb (Html5) or 80kb (GIF, JPG, PNG)
• Back-up image: 40kb (JPG or PNG). Back-up image only required if you supply an HTML5 banner.
• Looping: Yes
• See Half Page for more information.

I would like them to be quite simple , WYNDALE Your Faulconbridge property experts and another saying WYNDALE your Lawson property experts and WYNDALE your Hazelbrook property experts (3 different versions all up ) and another version MAREE DOLTON your Faulconbridge property expert with logo and her image , i've put a photo of the top banner example and a video of the side banner it has a video in the background that i will get produced if it works

```html
<!DOCTYPE html>
<html lang="en">
<head>
<meta charset="UTF-8">
<title>WYNDALE – Your Faulcon Bridge Property Experts</title>
<link rel="stylesheet" href="https://fonts.googleapis.com/css2?family=Poppins:wght@400;500;600&display=swap">
<style>
  :root {
    --scene-dark: #1d2a2c;
    --scene-mid: #3d5556;
    --scene-light: #7d8f8a;
    --scene-sky: #9fb0ad;
    --overlay: rgba(22, 40, 44, 0.45);
    --text-light: #ffffff;
  }
  * { margin: 0; padding: 0; box-sizing: border-box; }
  html, body {
    width: 1200px;
    height: 2400px;
    overflow: hidden;
    background: var(--scene-dark);
  }
  .skyscraper-ad {
    position: relative;
    width: 1200px;
    height: 2400px;
    overflow: hidden;
    font-family: "Poppins", sans-serif;
    color: var(--text-light);
  }
  .background-scene {
    position: absolute;
    inset: 0;
    background:
      linear-gradient(160deg, var(--scene-dark) 0%, var(--scene-mid) 30%, var(--scene-light) 55%, var(--scene-mid) 75%, var(--scene-dark) 100%);
  }
  .background-scene::after {
    content: "";
    position: absolute;
    inset: 0;
    background: radial-gradient(ellipse at 85% 20%, rgba(159,176,173,0.55) 0%, transparent 45%);
  }
  .tint-overlay {
    position: absolute;
    inset: 0;
    background: var(--overlay);
  }
  .brand-mark {
    position: absolute;
    top: 820px;
    left: 0;
    width: 100%;
    display: flex;
    justify-content: center;
    align-items: center;
    gap: 28px;
  }
  .brand-square {
    width: 56px;
    height: 56px;
    background: var(--text-light);
  }
  .brand-name {
    font-weight: 500;
    font-size: 76px;
    letter-spacing: 6px;
    line-height: 1;
  }
  .headline {
    position: absolute;
    top: 1240px;
    left: 0;
    width: 100%;
    text-align: center;
    line-height: 1;
  }
  .headline-intro {
    display: block;
    font-weight: 400;
    font-size: 112px;
    margin-bottom: 18px;
  }
  .headline-place {
    display: block;
    font-weight: 600;
    font-size: 106px;
    letter-spacing: -1px;
    margin-bottom: 20px;
  }
  .headline-tag {
    display: block;
    font-weight: 500;
    font-size: 100px;
    letter-spacing: -2px;
  }
</style>
</head>
<body>
  <div class="skyscraper-ad">
    <div class="background-scene" role="img" aria-label="Background video still: a man walking down steps from a timber pergola deck beside a modern home"></div>
    <div class="tint-overlay"></div>

    <div class="brand-mark">
      <span class="brand-square"></span>
      <span class="brand-name">WYNDALE</span>
    </div>

    <h1 class="headline">
      <span class="headline-intro">Your</span>
      <span class="headline-place">Faulcon Bridge</span>
      <span class="headline-tag">PropertyExperts</span>
    </h1>
  </div>
</body>
</html>
```